I need a design for box for a new product

We are a small business with many awards and loads of customers in the grooming/pet industry. I am attaching a color pattern/theme to go along with the box. The name of the product is MISTORA MAX: The Complete All-Round Spray Wand. It uses a blue infrared light to help kill 99% of bacteria, along with a canister to put a multitude of liquids/solutions in. It is ideal for sanitizing and protecting grooming salons, kennels, doggy daycare, boarding facilities, vet clinics, animal shelters, barns, and more! Some of the benefits of the Mistora Max are, but not limited to:
Continuous Spray that reaches over 6 feet in distance, a simple hold of the button for 2 seconds starts the autospray, a much easier alternative than spraying a pump bottle. Comes with a USB-C Charger and charging time only takes 2 hours for a full 50 minutes of run time.

Target Market(s)

Pet Industry Professionals

Industry/Entity Type

Pet Industry

Colors
F0912C
F2A743
F7CA91
FBE8D2
FDF5EE

Requirements
Must have
• A picture of our actual spray gun on the box, worked into the pattern - may need to be photoshopped a bit - do your magic

```html
<!DOCTYPE html>
<html lang="en">
<head>
<meta charset="utf-8">
<title>Mistora Max — Box Artwork</title>
<link rel="stylesheet" href="https://fonts.googleapis.com/css2?family=Michroma&family=Ubuntu:wght@500&family=Roboto+Condensed:wght@500&display=swap">
<style>
  :root {
    --bg: #e9e9e9;
    --orange: #cd6748;
    --orange-soft: #d8775a;
    --navy: #26313c;
    --navy-deep: #1e2831;
    --product-navy: #1f3158;
    --white: #f4f1ee;
  }
  * { margin: 0; padding: 0; box-sizing: border-box; }
  html, body {
    width: 1200px; height: 1200px; overflow: hidden;
    background: var(--bg);
  }
  .box-front {
    position: absolute;
    left: 110px; top: 170px;
    width: 880px; height: 860px;
    background: var(--navy);
    overflow: hidden;
  }
  .splatter-art {
    position: absolute; inset: 0;
    background:
      radial-gradient(ellipse 62% 48% at 40% 26%, var(--orange) 0 70%, transparent 100%),
      radial-gradient(ellipse 30% 30% at 14% 60%, var(--orange-soft) 0 45%, transparent 100%),
      linear-gradient(100deg, var(--orange) 0%, var(--orange) 55%, var(--navy) 80%, var(--navy-deep) 100%);
  }
  .title {
    position: absolute;
    left: 0; width: 840px; top: 150px;
    text-align: center;
    font-family: "Michroma", sans-serif;
    font-weight: 400;
    font-size: 50px;
    line-height: 60px;
    color: var(--white);
  }
  .title-rule {
    position: absolute;
    left: 235px; top: 226px;
    width: 370px; height: 2px;
    background: linear-gradient(90deg, transparent, var(--white) 20%, var(--white) 80%, transparent);
  }
  .subtitle {
    position: absolute;
    left: 0; width: 840px; top: 238px;
    text-align: center;
    font-family: "Ubuntu", sans-serif;
    font-weight: 500;
    font-size: 25px;
    line-height: 34px;
    color: var(--white);
  }
  .product-photo {
    position: absolute;
    left: 158px; top: 337px;
    width: 400px; height: 470px;
    border-radius: 40px 60px 20px 20px;
    background: linear-gradient(160deg, #2b4170 0%, var(--product-navy) 55%, #c9c9cc 100%);
  }
  .benefits {
    position: absolute;
    left: 495px; top: 460px;
    width: 385px; height: 385px;
    border-radius: 50%;
    background: var(--orange);
    display: flex; flex-direction: column;
    justify-content: center; align-items: center;
    padding: 0 24px;
    font-family: "Roboto Condensed", sans-serif;
    font-weight: 500;
    font-size: 15.5px;
    line-height: 20px;
    text-transform: uppercase;
    text-align: center;
    color: var(--white);
  }
  .benefits li {
    list-style: none;
    padding: 6px 0;
  }
  .benefits li + li {
    border-top: 1.5px solid rgba(244, 241, 238, 0.75);
  }
  .box-side {
    position: absolute;
    left: 990px; top: 170px;
    width: 100px; height: 860px;
    background: var(--navy-deep);
    display: flex;
    flex-direction: row;
    align-items: center;
    justify-content: center;
    gap: 10px;
  }
  .side-name, .side-tagline {
    writing-mode: vertical-rl;
    transform: rotate(180deg);
    color: var(--white);
    white-space: nowrap;
  }
  .side-name {
    font-family: "Michroma", sans-serif;
    font-size: 38px;
    line-height: 44px;
  }
  .side-tagline {
    font-family: "Ubuntu", sans-serif;
    font-weight: 500;
    font-size: 12px;
    line-height: 15px;
    text-align: center;
  }
</style>
</head>
<body>
  <main class="box-front">
    <div class="splatter-art" role="img" aria-label="Orange and dark navy paint splatter pattern"></div>

    <h1 class="title">MISTORA MAX</h1>
    <div class="title-rule"></div>
    <p class="subtitle">THE COMPLETE<br>ALL-ROUND SPRAY WAND</p>

    <div class="product-photo" role="img" aria-label="Photo of the navy cordless spray wand with clear liquid canister"></div>

    <ul class="benefits">
      <li>Continuous spray that<br>reaches over 6 feet in distance</li>
      <li>A much easier alternative than<br>spraying a pump bottle</li>
      <li>A simple hold of the button<br>for 2 seconds starts the autospray</li>
      <li>Comes with a USB-C charger and charging<br>time only takes 2 hours for a full 50<br>minutes of run time</li>
    </ul>
  </main>

  <aside class="box-side">
    <p class="side-name">MISTORA MAX</p>
    <p class="side-tagline">THE COMPLETE<br>ALL-ROUND SPRAY WAND</p>
  </aside>
</body>
</html>
```